Training Company Needs a Web Design

We are a Training company that needs a website design completed for us. "The Harbor Loft" The website will be a 'community space' specialising in 'Change and Transformation'. It will be a 'space' where individuals can come to find out 'latest news', upcoming events and courses, chat with others and find 'tools and templates'. They will need to login as a 'Member'.

The final design needs to be professional but have a 'fun and interactive' feel and appeal to our target audience who are predominantly corporate individuals.

Target Market(s)

Corporate Individuals - they may have a Change or Project background

Industry/Entity Type

Business Consultant

Number of Pages Required

3 page

Font styles to use
Sans Serif

Requirements
Must have
• Design for 'Home Page'
• A professional and corporate 'feel' but be fun and interactive.
Nice to have
• A 'sense' of how some of the other pages may be designed or laid out.

```html
<!DOCTYPE html>
<html lang="en">
<head>
<meta charset="utf-8">
<title>The Harbor Loft — Home</title>
<link rel="stylesheet" href="https://fonts.googleapis.com/css2?family=Tinos:wght@400;700&family=Open+Sans:wght@400;600;700&display=swap">
<style>
:root{
  --purple:#8c6bb1;
  --orange:#f04e23;
  --news-orange:#f15a2b;
  --sky:#0da0dc;
  --navy:#0b4f8f;
  --yellow:#f4c430;
  --tile-yellow:#f2cf3c;
  --teal:#1a8fc9;
  --ink:#333333;
  --body:#555555;
  --dark-brown:#3b2418;
  --footer:#3b3b3b;
  --white:#ffffff;
  --serif:"Tinos", "Times New Roman", serif;
  --sans:"Open Sans", Arial, sans-serif;
}
*{box-sizing:border-box;margin:0;padding:0}
h1,h2,h3{font-weight:400}
html,body{width:1200px;height:2812px;overflow:hidden;background:var(--white)}
body{position:relative;font-family:var(--sans);color:var(--ink)}
.page{position:relative;width:1200px;height:2812px}

/* header */
.site-header{position:absolute;left:0;top:0;width:1200px;height:131px;border-top:6px solid #333;background:var(--white)}
.brand{position:absolute;left:84px;top:34px;display:flex;align-items:center;gap:14px}
.brand-dot{width:26px;height:26px;border-radius:50%;background:var(--teal)}
.brand-name{font-family:var(--sans);font-weight:600;font-size:30px;color:var(--teal);line-height:1}
.account{position:absolute;right:84px;top:22px;font-family:var(--serif);font-size:17px;letter-spacing:1px;color:var(--orange);display:flex;align-items:center;gap:12px}
.main-nav{position:absolute;right:84px;top:78px;display:flex;gap:14px;font-family:var(--serif);font-weight:700;font-size:21px;letter-spacing:2px;color:var(--teal)}
.main-nav .current{color:var(--navy)}
.main-nav .slash{font-weight:400}

/* feature cards */
.feature{position:absolute;left:0;width:606px;color:var(--white)}
.feature-purple{top:131px;height:328px;background:var(--purple)}
.feature-orange{top:459px;height:325px;background:var(--orange)}
.feature-blue{top:784px;height:326px;background:var(--sky)}
.feature-icon{position:absolute;left:84px;top:28px;width:60px;height:64px}
.feature-body{position:absolute;left:174px;top:26px;width:400px}
.feature-title{font-family:var(--serif);font-weight:700;font-size:27px;line-height:36px;text-transform:uppercase}
.feature-text{margin-top:16px;width:350px;font-size:14px;line-height:26px;font-weight:600}
.pill{position:absolute;width:109px;height:38px;border-radius:19px;font-family:var(--serif);font-size:19px;letter-spacing:1px;display:flex;align-items:center;justify-content:center}
.feature .pill{left:478px;top:274px;background:var(--white);color:var(--ink)}

.hero-photo{position:absolute;left:606px;top:131px;width:594px;height:653px;background:linear-gradient(160deg,#5e5e5e 0%,#8a8a8a 40%,#3d3d3d 100%)}
.hero-caption{position:absolute;left:0;bottom:0;width:100%;height:62px;background:rgba(0,0,0,.55);color:var(--white);font-size:16px;font-weight:600;padding:20px 24px}
.hero-arrows{position:absolute;right:18px;bottom:20px;width:44px;height:22px}

.calendar{position:absolute;left:606px;top:788px;width:594px;height:322px;background:var(--navy);color:var(--white)}
.calendar-title{position:absolute;right:96px;top:14px;text-align:right;font-family:var(--serif);font-size:56px;line-height:64px;letter-spacing:4px}
.calendar-year{color:var(--yellow)}
.calendar-tab{position:absolute;left:0;bottom:0;width:220px;height:180px}

/* intro */
.intro-copy{position:absolute;left:84px;top:1158px;width:530px}
.intro-heading{font-family:var(--serif);font-size:40px;line-height:54px;letter-spacing:2px;color:var(--ink);white-space:nowrap}
.intro-tagline{margin-top:18px;width:480px;font-family:var(--serif);font-weight:700;font-size:24px;line-height:35px;letter-spacing:1px;text-transform:uppercase}
.t-orange{color:var(--orange)}.t-navy{color:var(--navy)}.t-sky{color:var(--sky)}.t-purple{color:var(--purple)}.t-yellow{color:var(--yellow)}.t-ink{color:var(--ink)}
.intro-text{margin-top:24px;width:510px;font-size:16px;line-height:30px;color:var(--body);letter-spacing:.5px}
.intro-text p+p{margin-top:30px}
.intro .pill{left:478px;top:1742px;background:var(--sky);color:var(--white)}

.tile{position:absolute;width:237px;height:300px}
.tile-photo{width:237px;height:225px}
.tile-label{height:75px;display:flex;align-items:center;justify-content:center;text-align:center;font-family:var(--serif);font-size:19px;line-height:24px;color:var(--white);text-transform:uppercase;padding:0 16px}
.tile-a{left:624px;top:1166px}.tile-b{left:877px;top:1166px}
.tile-c{left:624px;top:1481px}.tile-d{left:877px;top:1481px}

/* news */
.news{position:absolute;left:0;top:1834px;width:1200px;height:529px;background:var(--news-orange);color:var(--white)}
.news-heading{position:absolute;top:38px;width:100%;text-align:center;font-family:var(--serif);font-size:42px;letter-spacing:4px}
.news-item{position:absolute;left:84px;width:1032px;padding-bottom:22px;border-bottom:2px dotted rgba(255,255,255,.85)}
.news-item-1{top:130px}.news-item-2{top:300px}
.news-title{font-family:var(--serif);font-size:23px;letter-spacing:1.5px;color:var(--dark-brown);text-transform:uppercase;white-space:nowrap;overflow:hidden}
.news-text{margin-top:14px;font-size:17px;line-height:32px;font-weight:600;letter-spacing:.5px}
.news-more{font-family:var(--serif);font-weight:700;letter-spacing:2px;color:var(--dark-brown);margin-left:24px}
.news-arrows{position:absolute;left:576px;top:476px;width:48px;height:26px}

/* map + footer */
.location-map{position:absolute;left:0;top:2363px;width:1200px;height:271px;background:linear-gradient(90deg,#9fc3e8 0%,#b9d7a8 45%,#d9e6c4 55%,#a9cbec 100%)}
.site-footer{position:absolute;left:0;top:2634px;width:1200px;height:178px;background:var(--footer)}
.social{position:absolute;left:386px;top:47px;display:flex;gap:13px}
.social span{width:41px;height:41px;background:#cfcfcf;border-radius:3px}
.copyright{position:absolute;top:124px;width:100%;text-align:center;font-family:var(--serif);font-size:17px;letter-spacing:1px;color:var(--white)}
.copyright .brand-text{color:var(--orange)}
</style>
</head>
<body>
<div class="page">

  <header class="site-header">
    <div class="brand"><span class="brand-dot"></span><span class="brand-name">The Harbor Loft</span></div>
    <div class="account">
      <span>REGISTER</span><span>|</span><span>LOGIN</span>
      <svg width="18" height="20" viewBox="0 0 18 20" aria-hidden="true"><circle cx="9" cy="6" r="5" fill="#9aa9b5"/><path d="M0 20c0-6 4-8 9-8s9 2 9 8z" fill="#9aa9b5"/></svg>
    </div>
    <nav class="main-nav">
      <span class="current">HOME</span><span class="slash">/</span>
      <span>ABOUT US</span><span class="slash">/</span>
      <span>GALLERY</span><span class="slash">/</span>
      <span>NEWS</span><span class="slash">/</span>
      <span>CONTACTS</span>
    </nav>
  </header>

  <section class="feature feature-purple">
    <svg class="feature-icon" viewBox="0 0 60 64" aria-hidden="true">
      <path d="M30 2 58 14 30 26 2 14z" fill="#fff"/><rect x="52" y="14" width="3" height="16" fill="#fff"/>
      <circle cx="30" cy="32" r="11" fill="#fff"/><path d="M6 64c0-14 10-20 24-20s24 6 24 20z" fill="#fff"/>
    </svg>
    <div class="feature-body">
      <h2 class="feature-title">Consequuntur dolores<br>ratione voluptatem</h2>
      <p class="feature-text">Nemo enim ipsam voluptatem quia voluptas sit aspernatur aut odit aut fugit, sed quia consequuntur magni dolores eos qui ratione voluptatem sequi nesciunt. Neque porro quisquam est, qui dolorem ipsum quia dolor sit amet.</p>
    </div>
    <span class="pill">MORE</span>
  </section>

  <section class="feature feature-orange">
    <svg class="feature-icon" viewBox="0 0 60 64" aria-hidden="true">
      <rect x="4" y="10" width="52" height="12" rx="4" fill="none" stroke="#fff" stroke-width="4"/>
      <rect x="2" y="26" width="56" height="12" rx="4" fill="none" stroke="#fff" stroke-width="4"/>
      <rect x="4" y="42" width="52" height="12" rx="4" fill="none" stroke="#fff" stroke-width="4"/>
    </svg>
    <div class="feature-body">
      <h2 class="feature-title">Nonsequuntur magni<br>dolores ratione</h2>
      <p class="feature-text">Voluptatem quia voluptas sit aspernatur aut odit aut fugit, sed quia consequuntur magni dolores eos qui ratione voluptatem sequi nesciunt. Neque porro quisquam est, qui dolorem ipsum quia dolor sit amet.</p>
    </div>
    <span class="pill">MORE</span>
  </section>

  <section class="feature feature-blue">
    <svg class="feature-icon" viewBox="0 0 60 64" aria-hidden="true">
      <path d="M30 4C16 4 6 14 6 27c0 8 4 13 8 17v16h22v-8h8c4 0 6-2 6-6v-8h6l-6-12C50 14 42 4 30 4z" fill="#fff"/>
      <circle cx="24" cy="24" r="6" fill="none" stroke="#0da0dc" stroke-width="3"/>
      <circle cx="37" cy="32" r="4" fill="none" stroke="#0da0dc" stroke-width="3"/>
    </svg>
    <div class="feature-body">
      <h2 class="feature-title">Praesentium voluptatum<br>deleniti atque</h2>
      <p class="feature-text">Aspernatur aut odit aut fugit, sed quia consequuntur magni dolores eos qui ratione voluptatem sequi nesciunt. Neque porro quisquam est, qui dolorem ipsum quia dolor sit amet.</p>
    </div>
    <span class="pill">MORE</span>
  </section>

  <div class="hero-photo" role="img" aria-label="Black and white photo of students seated in a lecture hall, taking notes">
    <div class="hero-caption">Nam libero tempore, cum soluta nobis est eligendi</div>
    <svg class="hero-arrows" viewBox="0 0 44 22" aria-hidden="true">
      <path d="M14 3 6 11l8 8M30 3l8 8-8 8" fill="none" stroke="#bbb" stroke-width="3"/>
    </svg>
  </div>

  <section class="calendar">
    <h2 class="calendar-title">VIEW YOUR<br>EVENT<br>CALENDAR<br><span class="calendar-year">2016</span></h2>
    <svg class="calendar-tab" viewBox="0 0 220 180" aria-hidden="true">
      <path d="M0 0 220 180H0z" fill="#fff"/>
      <text x="12" y="50" transform="rotate(39 12 50)" font-family="Tinos, serif" font-weight="700" font-size="22" letter-spacing="3" fill="#333">CLICK HERE</text>
    </svg>
  </section>

  <section class="intro">
    <div class="intro-copy">
      <h2 class="intro-heading">QUOD MAXIME PLACEAT<br>FACERE POSSIMUS</h2>
      <p class="intro-tagline"><span class="t-orange">Nam libero tempore</span><span class="t-ink">, </span><span class="t-navy">cum soluta nobis</span><span class="t-ink">, </span><span class="t-sky">est eligendi</span><span class="t-ink">, </span><span class="t-purple">optio cumque</span><span class="t-ink">, </span><span class="t-yellow">nihil impedit</span></p>
      <div class="intro-text">
        <p>Sed ut perspiciatis unde omnis iste natus error sit voluptatem accusantium doloremque laudantium, totam eaque ipsa quae ab illo veritatis. Nemo enim ipsam voluptatem quia voluptas sit aspernatur sequuntur magni dolores eos qui ratione voluptatem sequi nesciunt.</p>
        <p>Neque porro quisquam est, qui dolorem ipsum quia dolor sit amet, consectetur, adipisci velit, sed quia non numquam eius modi tempora.</p>
      </div>
    </div>
    <span class="pill">MORE</span>

    <div class="tile tile-a">
      <div class="tile-photo" role="img" aria-label="Photo of students gathered around a laptop in a bright classroom" style="background:linear-gradient(160deg,#d8e3ec,#9aa6b2)"></div>
      <div class="tile-label" style="background:var(--orange)">New classroom technology</div>
    </div>
    <div class="tile tile-b">
      <div class="tile-photo" role="img" aria-label="Photo of an international student group meeting at a table" style="background:linear-gradient(160deg,#e4ebf1,#a4afba)"></div>
      <div class="tile-label" style="background:var(--navy)">International students</div>
    </div>
    <div class="tile tile-c">
      <div class="tile-photo" role="img" aria-label="Photo of new students working together at a desk" style="background:linear-gradient(160deg,#d5dde4,#8e99a4)"></div>
      <div class="tile-label" style="background:var(--tile-yellow)">New student orientation</div>
    </div>
    <div class="tile tile-d">
      <div class="tile-photo" role="img" aria-label="Photo of colleagues looking at a laptop in an office" style="background:linear-gradient(160deg,#dfe5ea,#9ba4ad)"></div>
      <div class="tile-label" style="background:var(--purple)">Career opportunities</div>
    </div>
  </section>

  <section class="news">
    <h2 class="news-heading">NEWS UPDATES</h2>
    <article class="news-item news-item-1">
      <h3 class="news-title">Neque porro quisquam est, qui dolorem ipsum</h3>
      <p class="news-text">Accusamus et iusto odio dignissimos ducimus qui blanditiis praesentium voluptatum deleniti atque corrupti quos dolores et quas molestias excepturi.<span class="news-more">MORE</span></p>
    </article>
    <article class="news-item news-item-2">
      <h3 class="news-title">Occaecati cupiditate non provident, similique sunt in culpa qui offi-</h3>
      <p class="news-text">Deserunt iusto odio dignissimos ducimus qui blanditiis praesentium voluptatum deleniti atque corrupti quos dolores et quas molestias excepturi.<span class="news-more">MORE</span></p>
    </article>
    <svg class="news-arrows" viewBox="0 0 48 26" aria-hidden="true">
      <path d="M20 3 9 13l11 10M28 3l11 10-11 10" fill="none" stroke="#2b2b2b" stroke-width="5"/>
    </svg>
  </section>

  <div class="location-map" role="img" aria-label="Map showing the location of the venue"></div>

  <footer class="site-footer">
    <div class="social" aria-label="Social links">
      <span></span><span></span><span></span><span></span><span></span><span></span><span></span><span></span>
    </div>
    <p class="copyright"><span class="brand-text">The Harbor Loft</span> © 2016 All Rights Reserved</p>
  </footer>

</div>
</body>
</html>
```